Beauty & Wellness business needs a flyer to describe a multitude of therapy

I would like a flyer to represent my company. i would like it to have the form of a pamphlet 6 pages. The flyer should be in french if possible, but english also is okay. I'll upload a word file that illustrate what i would like, but it can be of course other images, this is just an example. And the text includes all the services we provide, some small description might be added if you think it's worth it from design point of view.
Target Market(s)
The market is seasonal. it's mostly winter for skiers, so wealthy and sporty people, and attentive to nature. But i also want to promote the brand for locals all year long, with reasonable pricing.
Industry/Entity Type
Wellness & aesthetics
Look and feel

```html
<!DOCTYPE html>
<html lang="fr">
<head>
<meta charset="utf-8">
<title>Lumi's Studio – Dépliant</title>
<link rel="stylesheet" href="https://fonts.googleapis.com/css2?family=Playfair+Display:wght@400;500;600;700&display=swap">
<style>
:root{
  --plum:#7a1d60;
  --plum-dark:#671650;
  --magenta:#9c2a84;
  --ink:#5b1447;
  --text:#3a2a35;
  --paper:#ffffff;
  --stage:#d8d8da;
}
*{margin:0;padding:0;box-sizing:border-box}
html,body{width:1200px;height:2738px;overflow:hidden}
body{background:var(--stage);font-family:"Playfair Display",Georgia,serif;color:var(--text);position:relative}
.spread{position:absolute;left:100px;width:1000px;height:707px;background:var(--paper);box-shadow:0 4px 14px rgba(0,0,0,.25);overflow:hidden}
.spread--outside{top:632px}
.spread--inside{top:1399px}
.spread svg.bg{position:absolute;inset:0}
.abs{position:absolute;line-height:1.15;white-space:nowrap}
.h-panel{font-weight:600;font-size:23px;color:var(--plum-dark)}
.h-panel.light{color:#fff}
.list{position:absolute;list-style:none}
.list li{display:flex;align-items:center;gap:9px;font-size:14.5px;height:22.7px}
.list li::before{content:"";width:11px;height:11px;border:1.5px solid currentColor;border-radius:50%;opacity:.8;flex:none}
.list.light li{color:#fff}
.list.dark li{color:var(--text)}
.list.purple li{color:var(--ink)}
.photo{position:absolute;border-radius:50%;border:6px solid #fff;box-shadow:0 0 0 3px var(--plum),0 3px 8px rgba(0,0,0,.2)}
.about{position:absolute;left:358px;top:54px;width:290px;font-size:11.6px;line-height:14.1px;text-align:justify;color:var(--text)}
.about p+p{margin-top:14px}
.brand{position:absolute;display:flex;align-items:center;justify-content:center;gap:10px;font-size:17px;font-weight:600;letter-spacing:4px;text-transform:uppercase}
.brand::before{content:"";width:22px;height:22px;border-radius:50%;border:2px solid currentColor}
.contact-title{position:absolute;left:333px;width:334px;text-align:center;top:491px;color:#fff;font-size:16px;letter-spacing:2px}
.phone{position:absolute;left:361px;top:525px;width:282px;height:50px;border:2px solid #fff;color:#fff;font-size:31px;display:flex;align-items:center;justify-content:center}
.contact-row{position:absolute;left:368px;display:flex;align-items:center;gap:16px;color:#fff;font-size:15px}
.contact-row svg{width:18px;height:18px;flex:none}
.cover-title{position:absolute;left:667px;width:333px;text-align:center;color:#fff;font-size:32px;font-weight:500;line-height:38px}
.rule{position:absolute;left:795px;width:78px;height:2px;background:#fff}
.url{position:absolute;left:667px;width:333px;text-align:center;color:#fff;font-size:13px;letter-spacing:2px}
.svc-h{font-size:18px;font-weight:600}
.svc-p{font-size:11.5px;font-weight:600;line-height:14px;white-space:normal;width:285px}
.light{color:#fff}
.purple{color:var(--ink)}
.big-h{font-size:22px;font-weight:600;color:var(--magenta)}
.bold-h{font-size:17px;font-weight:700;color:var(--plum)}
</style>
</head>
<body>

<!-- Outside of the leaflet -->
<section class="spread spread--outside">
  <svg class="bg" width="1000" height="707" viewBox="0 0 1000 707">
    <defs>
      <linearGradient id="fold" x1="0" x2="1">
        <stop offset="0" stop-color="#ffffff"/><stop offset=".8" stop-color="#f2f2f3"/><stop offset="1" stop-color="#e2e2e4"/>
      </linearGradient>
    </defs>
    <rect x="0" y="0" width="333" height="707" fill="url(#fold)"/>
    <rect x="333" y="0" width="334" height="707" fill="url(#fold)"/>
    <rect x="667" y="0" width="333" height="707" fill="url(#fold)"/>
    <path d="M0 360 C120 320 220 400 330 340 C450 280 560 300 700 320 C820 335 900 280 1000 250" fill="none" stroke="var(--magenta)" stroke-width="9"/>
    <path d="M0 378 C120 338 220 418 330 358 C450 298 560 318 700 338 C820 353 900 298 1000 268 L1000 707 L0 707 Z" fill="var(--plum)"/>
    <path d="M333 350 C450 298 560 318 667 333 L667 707 L333 707 Z" fill="var(--plum-dark)"/>
  </svg>

  <h2 class="abs h-panel" style="left:23px;top:20px">Nos massages maisons</h2>
  <ul class="list dark" style="left:23px;top:56px">
    <li>Sportif</li><li>Pierre chaude</li><li>AryuvédiquePindas</li><li>Guasha</li><li>Bambou</li><li>Drainage lymphatique</li><li>Pour femmes enceintes</li><li>Réflexologie</li><li>Relaxant</li><li>Shiatsu</li><li>Deep tissue</li><li>Méso Cellulite</li>
  </ul>
  <div class="photo" role="img" aria-label="Photo d'un massage du dos" style="left:110px;top:303px;width:200px;height:200px;background:radial-gradient(circle at 40% 40%,#e7c3aa,#a9725a 70%,#3c2a28)"></div>
  <div class="photo" role="img" aria-label="Photo d'un massage aux pochons d'herbes" style="left:20px;top:424px;width:190px;height:190px;background:radial-gradient(circle at 50% 50%,#f2dcc8,#cf9b7a 70%,#a8705a)"></div>
  <div class="photo" role="img" aria-label="Photo d'un traitement anti-cellulite" style="left:159px;top:548px;width:144px;height:144px;background:radial-gradient(circle at 50% 55%,#e0b193,#b88168 70%,#7a4e42)"></div>

  <h2 class="abs h-panel" style="left:358px;top:22px">À PROPOS DE NOUS</h2>
  <div class="about">
    <p>Je suis ravie de vous présenter ma gamme complète de services de soins du corps et du visage, ainsi que des soins esthétiques de haute qualité. Au Lumi's Studio, vous trouverez un espace intime et émotionnel. Ma philosophie a toujours été de se sentir bien dans sa peau, afin de vivre une vie épanouie. C'est pourquoi je vous offre mes connaissances et plus de 20 ans d'expérience dans les thérapies alternatives et les soins esthétiques.</p>
    <p>Ma mission est de vous aider à vous sentir mieux dans votre corps et votre esprit en vous offrant des soins de qualité adaptés à vos besoins et préférences. Que vous cherchiez à vous détendre, à vous rafraîchir ou à vous revitaliser, je suis là pour vous aider à atteindre vos objectifs.</p>
  </div>
  <div class="brand light" style="left:333px;width:334px;top:438px">Lumi's Studio</div>
  <div class="contact-title">Contact Information</div>
  <div class="phone">+41-79 000 1234</div>
  <div class="contact-row" style="top:590px">
    <svg viewBox="0 0 24 24"><path d="M12 2a7 7 0 0 0-7 7c0 5 7 13 7 13s7-8 7-13a7 7 0 0 0-7-7zm0 9.5A2.5 2.5 0 1 1 12 6.5a2.5 2.5 0 0 1 0 5z" fill="#fff"/></svg>
    <span>Chemin des Alpes 12, Montval, Suisse</span>
  </div>
  <div class="contact-row" style="top:622px">
    <svg viewBox="0 0 24 24"><rect x="2" y="5" width="20" height="14" rx="1" fill="#fff"/><path d="M2 6l10 7 10-7" fill="none" stroke="var(--plum-dark)" stroke-width="1.8"/></svg>
    <span>contact@lumi-studio.example</span>
  </div>
  <div class="contact-row" style="top:650px">
    <svg viewBox="0 0 24 24"><circle cx="12" cy="12" r="9.5" fill="none" stroke="#fff" stroke-width="2"/><path d="M2.5 12h19M12 2.5c3 3 3 16 0 19M12 2.5c-3 3-3 16 0 19" fill="none" stroke="#fff" stroke-width="1.6"/></svg>
    <span>www.lumi-studio.example</span>
  </div>

  <div class="brand purple" style="left:667px;width:333px;top:125px">Lumi's Studio</div>
  <div class="photo" role="img" aria-label="Photo d'une femme en peignoir appliquant une crème" style="left:711px;top:162px;width:244px;height:244px;background:radial-gradient(circle at 50% 45%,#f4ece8,#d9c6be 60%,#b59a90)"></div>
  <div class="photo" role="img" aria-label="Photo d'un soin masque du visage" style="left:690px;top:394px;width:140px;height:140px;background:radial-gradient(circle at 50% 45%,#f1ddd0,#cc8f82 70%,#9b4f5a)"></div>
  <div class="photo" role="img" aria-label="Photo d'une femme détendue au spa" style="left:838px;top:394px;width:140px;height:140px;background:radial-gradient(circle at 50% 45%,#efe6e2,#c5aaa0 70%,#8b6e68)"></div>
  <h1 class="cover-title" style="top:572px">L'atelier de Lumi<br>Soins de beauté</h1>
  <div class="rule" style="top:660px"></div>
  <div class="url" style="top:682px">www.lumi-studio.example</div>
</section>

<!-- Inside of the leaflet -->
<section class="spread spread--inside">
  <svg class="bg" width="1000" height="707" viewBox="0 0 1000 707">
    <defs>
      <linearGradient id="fold2" x1="0" x2="1">
        <stop offset="0" stop-color="#ffffff"/><stop offset=".8" stop-color="#f1f1f2"/><stop offset="1" stop-color="#e0e0e2"/>
      </linearGradient>
    </defs>
    <rect x="0" y="0" width="333" height="707" fill="url(#fold2)"/>
    <rect x="333" y="0" width="334" height="707" fill="url(#fold2)"/>
    <rect x="667" y="0" width="333" height="707" fill="url(#fold2)"/>
    <path d="M0 0 H1000 V305 C900 320 780 335 667 350 C560 365 450 390 333 410 C220 428 110 410 0 425 Z" fill="var(--plum)"/>
    <path d="M333 0 H667 V300 C600 300 530 315 470 335 C420 352 380 362 333 370 Z" fill="url(#fold2)"/>
    <path d="M0 425 C110 410 220 428 333 410 C450 390 560 365 667 350 C780 335 900 320 1000 305" fill="none" stroke="var(--magenta)" stroke-width="8" transform="translate(0 14)"/>
  </svg>

  <h2 class="abs h-panel light" style="left:21px;top:20px">Manicure &amp; Pédicure</h2>
  <ul class="list light" style="left:21px;top:59px">
    <li>Semi permanent</li><li>Gel</li><li>Fibre de verre</li>
  </ul>
  <div class="photo" role="img" aria-label="Photo d'un soin du visage avec masque" style="left:39px;top:146px;width:264px;height:264px;background:radial-gradient(circle at 50% 50%,#f7efe9,#e3cbbd 60%,#b98f7e)"></div>
  <div class="photo" role="img" aria-label="Photo de mains pendant une manucure" style="left:274px;top:273px;width:211px;height:211px;background:radial-gradient(circle at 50% 50%,#f5e3d9,#e2b9a4 65%,#c88f7b)"></div>
  <div class="photo" role="img" aria-label="Photo d'un œil et d'un sourcil dessiné" style="left:479px;top:278px;width:158px;height:158px;background:radial-gradient(circle at 50% 50%,#e9d8cf,#c5a594 65%,#8f6b5c)"></div>

  <h2 class="abs h-panel purple" style="left:24px;top:463px">Spa des pieds</h2>
  <ul class="list dark" style="left:21px;top:498px">
    <li>Argile thérapie</li><li>Paraffine</li><li>Plasma</li>
  </ul>
  <div class="abs bold-h" style="left:21px;top:592px">Épilation masculine et féminine</div>
  <div class="abs bold-h" style="left:21px;top:621px">Design des sourcils</div>

  <h2 class="abs h-panel purple" style="left:358px;top:18px">Nos traitements du visage</h2>
  <ul class="list purple" style="left:357px;top:58px">
    <li>Soin du visage classique</li><li>Fils de collagènes</li><li>Thérapie au plâtre</li><li>Plasma Lift</li><li>Chromothérapie</li><li>Aromathérapie</li><li>Needling</li>
  </ul>
  <div class="abs big-h" style="left:358px;top:527px">Thérapie Corporelle</div>
  <div class="abs svc-h" style="left:358px;top:570px;color:var(--magenta);font-size:16px">Massage</div>
  <div class="abs svc-p" style="left:358px;top:598px;color:var(--text)">Je propose plusieurs types de massages : Sports, pierres chaudes, bambou, pindas ayurvédiques, guasha, drainage lymphatique et relaxation.</div>

  <div class="abs svc-h light" style="left:690px;top:18px">Aromathérapie</div>
  <div class="abs svc-p light" style="left:690px;top:48px">Apaisez votre esprit avec nos services d' aromathérapie relaxants.</div>
  <div class="abs svc-h light" style="left:690px;top:103px">Chromothérapie</div>
  <div class="abs svc-p light" style="left:690px;top:135px">Soignez avec la couleur ! La chromothérapie apporte bien-être et équilibre au corps.</div>
  <div class="abs svc-h light" style="left:690px;top:194px">Réflexologie</div>
  <div class="abs svc-p light" style="left:690px;top:226px">Faites l'expérience de la relaxation et de la guérison grâce à la réflexologie.</div>

  <div class="abs svc-h" style="left:690px;top:397px;color:var(--magenta)">Mésothérapie</div>
  <div class="abs svc-p" style="left:690px;top:427px;color:var(--text)">Traitement avancé pour le rajeunissement de la peau. Il améliore la texture et l'apparence.</div>
  <div class="abs svc-h" style="left:690px;top:484px;color:var(--magenta)">Corps vers le haut</div>
  <div class="abs svc-p" style="left:690px;top:514px;color:var(--text)">Traitement pour améliorer la taille et la forme des fessiers.</div>
  <div class="abs big-h" style="left:690px;top:566px">THÉRAPIE DE LA PEAU</div>
  <div class="abs big-h" style="left:690px;top:606px">ESTHÉTIQUE</div>
</section>

</body>
</html>
```